Velmora - 3D medical animations and high end visual content

Our company creates high end visual content and animations for medical global companies.
Our website - www.velmora-studio.example
We would like to have an amazing business card for our CEO that he can use in the following exhebitions he is going to attend.
It is very important that the design will be memorable and diffrent. It has to reflect our brand design (you can have it from our website)
We would like to transmit innovation, prestige, luxury, aesthetics.
The card has to be Double Sided

Target Market(s)

Marketing managers in medical global companys

Industry/Entity Type

It Company

Contact Information for Business Card

Requirements
Nice to have
• It is very important that the design will be memorable and diffrent. It has to reflect our brand design (you can have it from our website)

```html
<!DOCTYPE html>
<html lang="en">
<head>
<meta charset="utf-8">
<title>Velmora — Business Card</title>
<link rel="stylesheet" href="https://fonts.googleapis.com/css2?family=Open+Sans:wght@400;600;700&display=swap">
<style>
  :root {
    --stage: #000000;
    --card: #1a1a1a;
    --white: #ffffff;
    --text-muted: #c9c9c9;
    --accent: #2ea9c6;
    --rule: #3f6670;
  }
  * { margin: 0; padding: 0; box-sizing: border-box; }
  html, body { width: 1200px; height: 900px; overflow: hidden; background: var(--stage); }
  body { position: relative; font-family: "Open Sans", Arial, sans-serif; }

  .card {
    position: absolute;
    top: 275px;
    width: 477px;
    height: 294px;
    background: var(--card);
  }
  .card--front { left: 116px; border-radius: 0 58px 0 58px; }
  .card--back  { left: 622px; border-radius: 58px 0 58px 0; }

  .brand-name {
    position: absolute;
    font-weight: 600;
    color: var(--white);
    letter-spacing: 2px;
    line-height: 1;
    text-transform: uppercase;
  }
  .card--front .brand-name { right: 28px; top: 54px; font-size: 40px; }
  .card--back  .brand-name { left: 0; right: 0; top: 118px; text-align: center; font-size: 42px; }

  .holder { position: absolute; left: 35px; top: 139px; }
  .holder__name {
    font-size: 18px; font-weight: 700; color: var(--accent);
    letter-spacing: 0.3px; line-height: 22px;
  }
  .holder__title { font-size: 13px; color: var(--text-muted); line-height: 18px; }
  .holder__rule {
    position: absolute; left: 142px; right: 31px; top: 167px;
    height: 1px; background: var(--rule);
  }

  .contacts {
    position: absolute; right: 30px; top: 183px;
    list-style: none;
  }
  .contacts li {
    display: flex; align-items: center; justify-content: flex-end;
    height: 19.7px;
    font-size: 13px; color: var(--text-muted);
  }
  .contacts svg { width: 10px; height: 10px; margin-left: 7px; fill: var(--accent); }
</style>
</head>
<body>
  <section class="card card--front">
    <div class="brand-name">Velmora</div>

    <div class="holder">
      <div class="holder__name">ELAN MARKOVITZ</div>
      <div class="holder__title">Founder &amp; CEO</div>
    </div>
    <div class="holder__rule"></div>

    <ul class="contacts">
      <li>+972-50-1234567
        <svg viewBox="0 0 10 10" aria-hidden="true"><path d="M2.5 0h5a1 1 0 0 1 1 1v8a1 1 0 0 1-1 1h-5a1 1 0 0 1-1-1V1a1 1 0 0 1 1-1zm0.5 1.3v6.4h4V1.3z"/></svg>
      </li>
      <li>+972-70-7654321
        <svg viewBox="0 0 10 10" aria-hidden="true"><path d="M2 0.5l1.8 2.2-1 1.1c.6 1.3 1.7 2.4 3 3l1.1-1L9.5 7.6 8.6 9.5C4.5 9.3.7 5.5.5 1.4z"/></svg>
      </li>
      <li>elan@velmora-studio.example
        <svg viewBox="0 0 10 10" aria-hidden="true"><path d="M0 2h10v6H0zM.8 2.6 5 5.6l4.2-3z" fill-rule="evenodd"/></svg>
      </li>
      <li>www.velmora-studio.example
        <svg viewBox="0 0 10 10" aria-hidden="true"><circle cx="5" cy="5" r="4.5"/></svg>
      </li>
    </ul>
  </section>

  <section class="card card--back">
    <div class="brand-name">Velmora</div>
  </section>
</body>
</html>
```